Naturopath specialising in Children's Health

I have just started working in a new clinic where I will be predominantly treating children so I would like to rebrand with a business card that reflects this.

I would like a clever design which is subtly playful and will attract children and parents alike, while maintaining a professional look. It must also reflect that I utilize natural medicine - including herbal medicine and nutrition as part of my treatment. Employing the use of a plant or herb would be ideal. I had envisioned the image of a dandelion blowing in the wind (or being blown by a child) as a great combination of the playful yet natural medicine I am trying to ecompass in the card.

I would like to use yellow, orange, blue or green as the dominant colour for the card.

The front of the card should contain the logo and the words 'Maribel Stroud - Naturopath.'

The back of the card should contain the following details:
Maribel Stroud BHSc Nat, Dip RM
Naturopath, Herbalist, Nutritionist, Iridologist, Remedial Massage Therapist, Reiki Practitioner
0413 927 186
Willowfern Haven - (02) 9731 4068
maribel.stroud@kestrelmail.example
NHPA 81347

Industry/Entity Type

Clinic

```html
<!DOCTYPE html>
<html lang="en">
<head>
<meta charset="utf-8">
<title>Maribel Stroud – Naturopath Business Card</title>
<link rel="stylesheet" href="https://fonts.googleapis.com/css2?family=Questrial&display=swap">
<style>
  :root {
    --page-bg: #ffffff;
    --leather-light: #8a5a3a;
    --leather-mid: #6b4129;
    --leather-dark: #4a2a18;
    --leaf-green: #a6d43a;
    --text-cream: #f3ece4;
    --shadow-brown: rgba(40, 20, 10, 0.42);
    --card-radius: 26px;
  }
  * { box-sizing: border-box; margin: 0; padding: 0; }
  html, body {
    width: 1200px;
    height: 900px;
    overflow: hidden;
    background: var(--page-bg);
  }
  body {
    font-family: "Questrial", "Century Gothic", sans-serif;
    position: relative;
  }
  .card {
    position: absolute;
    top: 295px;
    width: 540px;
    height: 310px;
    border-radius: var(--card-radius);
    overflow: hidden;
    background:
      radial-gradient(ellipse at 35% 30%, rgba(150, 100, 66, 0.55), transparent 60%),
      radial-gradient(ellipse at 80% 85%, rgba(40, 22, 12, 0.45), transparent 65%),
      linear-gradient(135deg, var(--leather-light), var(--leather-mid) 55%, var(--leather-dark));
    box-shadow: 0 14px 28px rgba(0, 0, 0, 0.18);
  }
  .card--front { left: 45px; }
  .card--back { left: 615px; }

  /* Front: brand lockup */
  .front-brand {
    position: absolute;
    left: 0;
    right: 0;
    top: 58px;
    display: flex;
    flex-direction: column;
    align-items: center;
    color: var(--leaf-green);
  }
  .front-brand__mark {
    width: 62px;
    height: 62px;
    border-radius: 50%;
    background: var(--leaf-green);
    margin-bottom: 18px;
  }
  .front-brand__name {
    font-size: 52px;
    line-height: 1;
    letter-spacing: 1px;
  }
  .front-brand__role {
    margin-top: 14px;
    font-size: 22px;
    letter-spacing: 14px;
    padding-left: 14px;
  }

  /* Back: faint decorative area and details */
  .back-decoration {
    position: absolute;
    left: 18px;
    top: 70px;
    width: 210px;
    height: 240px;
    border-radius: 48% 48% 0 0;
    background: radial-gradient(ellipse at 45% 45%, var(--shadow-brown), transparent 72%);
  }
  .back-details {
    position: absolute;
    top: 50px;
    left: 170px;
    right: 20px;
    text-align: center;
    color: var(--text-cream);
  }
  .back-details__name {
    color: var(--leaf-green);
    font-size: 19px;
    margin-bottom: 8px;
  }
  .back-details__roles {
    font-size: 10.5px;
    line-height: 1.55;
    margin-bottom: 10px;
  }
  .back-details__mobile {
    font-size: 18px;
    letter-spacing: 0.5px;
    margin-bottom: 12px;
  }
  .back-details__clinic {
    font-size: 12.5px;
  }
  .back-details__clinic-phone {
    font-size: 19px;
    letter-spacing: 0.5px;
    margin-bottom: 12px;
  }
  .back-details__email {
    font-size: 12px;
    margin-bottom: 10px;
  }
  .back-details__membership {
    font-size: 11.5px;
  }
</style>
</head>
<body>
  <section class="card card--front" aria-label="Business card front">
    <div class="front-brand">
      <div class="front-brand__mark" aria-hidden="true"></div>
      <div class="front-brand__name">Maribel Stroud</div>
      <div class="front-brand__role">Naturopath</div>
    </div>
  </section>

  <section class="card card--back" aria-label="Business card back">
    <div class="back-decoration" role="img" aria-label="Faint shadowed silhouette of a child blowing a dandelion"></div>
    <div class="back-details">
      <p class="back-details__name">Maribel Stroud BHSc Nat, Dip RM</p>
      <p class="back-details__roles">Naturopath, Herbalist, Nutritionist, Iridologist<br>Remedial Massage Therapist, Reiki Practitioner</p>
      <p class="back-details__mobile">0413 927 186</p>
      <p class="back-details__clinic">Willowfern Haven</p>
      <p class="back-details__clinic-phone">(02) 9731 4068</p>
      <p class="back-details__email">maribel.stroud@kestrelmail.example</p>
      <p class="back-details__membership">NHPA 81347</p>
    </div>
  </section>
</body>
</html>
```